International Travel & Visas Firm needs a Schengen Visa eBook Cover Design

We need an ebook cover design for an online based travel, immigration, visas & nationality law firm called 'OrB' (orbit and borderway). We are all about helping people overcome the obstacles to travel and ensuring that people achieve their dreams and ambitions through travel to various destinations and bettering their lives.This initial ebook cover is for our downloaded pdf ebook all about Schengen visas and travelling to any of the 26 European countries that form the Schengen Zone.We want people to be excited about buying this book even before receiving it.We would like to see amazing designs that also speak to our logo and new branding.Check out https://orbitandborderway.example/schengen-visas/ and http://orbitandborderway.pages.funnelvex.example/start-your-schengen-visa-application

Target Market(s)

Travellers that want to get a visa to travel around Europe

Industry/Entity Type

Travel Industry

Colors
fbee3d
faa54b

Requirements
Must have
• - Title:
• Passport Path Primer
Nice to have
• - tagline:
• Unshackle your feet and roam 26 European Countries
• - OrB Logo
• - Reference to it being an insider's guide to Schengen Visas
• - a play on the word OrB (I am)

```html
<!DOCTYPE html>
<html lang="en">
<head>
<meta charset="utf-8">
<title>Passport Path Primer — OrB</title>
<link rel="stylesheet" href="https://fonts.googleapis.com/css2?family=Caveat+Brush&family=Montserrat:wght@400;600;700&display=swap">
<style>
  :root {
    --scene-dark: #2b2824;
    --scene-warm: #7a5a3a;
    --scene-paper: #a98258;
    --band-orange: #f39a1a;
    --band-orange-deep: #e08a12;
    --ink-white: #ffffff;
    --mark-dark: #45454a;
  }
  * { margin: 0; padding: 0; box-sizing: border-box; }
  html, body { width: 750px; height: 1200px; overflow: hidden; background: var(--scene-dark); }
  .cover { position: relative; width: 750px; height: 1200px; overflow: hidden; }
  .cover__scene {
    position: absolute; inset: 0;
    background:
      radial-gradient(ellipse 260px 360px at 720px 520px, #1c1c1e 0%, rgba(28,28,30,0) 100%),
      linear-gradient(180deg, var(--scene-dark) 0%, #3a3028 30%, var(--scene-warm) 55%, var(--scene-paper) 80%, #8a6a48 100%);
  }
  .cover__band {
    position: absolute; top: 0; left: 111px; width: 528px; height: 1200px;
    background: linear-gradient(180deg, var(--band-orange-deep) 0%, var(--band-orange) 45%, #f5a21f 100%);
    color: var(--ink-white); text-align: center;
  }
  .tagline__lead {
    position: absolute; top: 102px; left: 0; right: 0;
    font: 400 16px/1 'Montserrat', sans-serif; letter-spacing: 5.4px; text-transform: uppercase;
  }
  .tagline__rule {
    position: absolute; top: 142px; left: 36px; right: 36px; height: 2px; background: var(--ink-white);
  }
  .tagline__count {
    position: absolute; top: 162px; left: 0; right: 0;
    font: 600 21px/1 'Montserrat', sans-serif; letter-spacing: 5.6px; text-transform: uppercase;
  }
  .tagline__dot { display: inline-block; width: 4px; height: 4px; border-radius: 50%; background: var(--ink-white); vertical-align: middle; margin: 0 14px; }
  .title {
    position: absolute; top: 340px; left: -10px; right: -10px;
    font: 400 150px/150px 'Caveat Brush', cursive; color: var(--ink-white);
  }
  .title span { display: block; }
  .brand { position: absolute; top: 1012px; left: 0; right: 0; display: flex; flex-direction: column; align-items: center; }
  .brand__row { display: flex; align-items: center; gap: 14px; }
  .brand__square { width: 22px; height: 22px; background: var(--mark-dark); }
  .brand__name { font: 700 80px/1 'Montserrat', sans-serif; color: var(--ink-white); }
  .brand__sub { margin-top: 10px; font: 700 15px/1 'Montserrat', sans-serif; color: var(--ink-white); letter-spacing: 0.5px; }
</style>
</head>
<body>
  <main class="cover">
    <div class="cover__scene" role="img" aria-label="Travel still life: vintage film camera, old world map and scattered postcards on a wooden desk"></div>
    <section class="cover__band">
      <p class="tagline__lead">Unshackle your feet and roam</p>
      <div class="tagline__rule"></div>
      <p class="tagline__count"><span class="tagline__dot"></span>26 European Countries<span class="tagline__dot"></span></p>
      <h1 class="title"><span>Passport</span><span>Path</span><span>Primer</span></h1>
      <div class="brand">
        <div class="brand__row">
          <span class="brand__square"></span>
          <span class="brand__name">OrB</span>
        </div>
        <p class="brand__sub">orbit and borderway</p>
      </div>
    </section>
  </main>
</body>
</html>
```